Brightgate Automotive Service Website Design

We are working with Brightgate Automotive Service. They are a local mechanic/garage and in need of a new website design.

Some sites to use for inspiration:

https://www.torvalle.example
https://www.quenby.example
https://parks-carcare.example
https://www.hollowmerefullautocare.example/

Thank you for taking the time to consider designing a website for us. We are web developers based in Stockton, CA, USA. Most of our projects go through the same process. Understanding this process may help you win a project with us. We custom-code all of our websites in-house. We don’t have any requirements as to what tools you use for your design, but we prefer Figma files. For any design that we label as four-stars, we send it to the client for review. The client picks the final design they want us to use. Once we complete this process, we will continue to show additional clients all the four-star sites and purchase them later. Your designs will have multiple chances to sell. For better chances of success, we ask that you follow these guidelines.

IMAGES:
If you use any images or icons in the design, we ask that you have a link to the asset so we can purchase the image/icon. Most of the designs we submit do not have the customer’s images on them unless they have some great images. Be creative; show us the feeling you are trying to portray with your image choices. Use any royalty-free site you choose. We subscribe to Adobe and mainly use their images, but we can purchase images outside of Adobe.

PLEASE NOTE: we will not submit designs to clients with watermarks on the images.

FONTS:
We ask that you identify the fonts used in the design. This can be done in a message if you want. We typically use Google Fonts and Adobe Fonts.

CONTENT:
We're always open to different content and ideas. We often submit designs with stock images so the client can see our vision. We typically take pictures after the website launch to use their images with our vision. Lorem Ipsum is fine for paragraphs, but we ask that you write the headers in correct English. We want to be able to show the vision and identify the sections of the website.

INSPIRATION:
We typically add a couple of links in the brief of websites we like to help you get started in your design.

REVISIONS:
We do not often ask for revisions of the designs unless we see something in the design that may not appeal to the client. If there are slight changes that we want to make, we do that in the development process.

FEEDBACK:
We rarely give feedback on designs during the design process. We are working on many website projects and do not have the time to provide feedback. We usually respond if your request is well thought out and asks specific questions, but a note asking “feedback, please” usually goes unanswered.

```html
<!DOCTYPE html>
<html lang="en">
<head>
<meta charset="utf-8">
<title>Brightgate Automotive Service</title>
<link href="https://fonts.googleapis.com/css2?family=Roboto:ital,wght@0,400;0,500;0,700;0,900;1,400&display=swap" rel="stylesheet">
<style>
:root{
  --red:#ee1c25;
  --red-soft:#f7a1a5;
  --ink:#111111;
  --text:#333333;
  --muted:#777777;
  --line:#d9d9d9;
  --light:#f4f4f4;
  --dark:#1b1b1b;
  --footer:#151515;
  --white:#ffffff;
}
*{box-sizing:border-box;margin:0;padding:0}
html,body{width:1200px;height:5376px;overflow:hidden}
body{font-family:'Roboto',sans-serif;color:var(--text);background:var(--white);position:relative}
.abs{position:absolute}
.photo{position:absolute}

/* top bar */
.topbar{position:absolute;left:0;top:0;width:1200px;height:38px;background:var(--ink);color:var(--white);font-size:12px;font-weight:700}
.topbar .follow{position:absolute;left:69px;top:12px;display:flex;gap:12px;align-items:center}
.topbar .dot{width:7px;height:7px;background:var(--white);display:inline-block}
.topbar .right{position:absolute;right:130px;top:12px;display:flex;gap:26px}
.topbar .search{position:absolute;right:0;top:0;width:70px;height:38px;background:var(--red);display:flex;align-items:center;justify-content:center}

/* header */
.header{position:absolute;left:0;top:38px;width:1200px;height:92px;background:var(--white);border-bottom:1px solid #eee}
.logo-block{position:absolute;left:0;top:0;width:420px;height:92px;background:var(--red);clip-path:polygon(0 0,100% 0,94% 100%,0 100%)}
.brand{position:absolute;left:69px;top:26px;font-size:38px;font-weight:700;color:var(--white);letter-spacing:1px}
.info{position:absolute;top:22px;display:flex;gap:14px;font-size:13px;color:var(--text)}
.info b{display:block;font-weight:500;color:var(--ink)}
.info i{font-style:italic}

/* nav */
.nav{position:absolute;left:0;top:130px;width:1200px;height:43px;background:var(--white)}
.nav a{position:absolute;top:14px;font-size:13px;color:var(--ink);text-decoration:none;font-weight:500}
.nav a.active{color:var(--red)}
.nav a.active:after{content:"";position:absolute;left:50%;margin-left:-8px;bottom:-14px;width:16px;height:3px;background:var(--red)}
.book{position:absolute;left:964px;top:0;width:166px;height:43px;background:var(--red);color:var(--white);font-weight:700;font-size:13px;display:flex;align-items:center;justify-content:center}

/* hero */
.hero{position:absolute;left:0;top:173px;width:1200px;height:637px;background:radial-gradient(ellipse at 80% 40%,#1f5fb8 0%,#0b1f4d 40%,#050c22 80%)}
.hero .car{position:absolute;right:0;top:170px;width:640px;height:380px;background:radial-gradient(ellipse at 55% 55%,#ff3b30 0%,#c4121a 45%,rgba(196,18,26,0) 72%)}
.hero h1{position:absolute;left:69px;top:142px;color:var(--white);font-size:60px;font-weight:700;line-height:74px}
.hero p{position:absolute;left:69px;top:306px;width:560px;color:var(--white);font-size:15px;font-weight:500;line-height:20px}
.btn-outline{position:absolute;left:69px;top:394px;width:156px;height:44px;background:var(--white);color:var(--red);font-size:14px;font-weight:700;display:flex;align-items:center;justify-content:center;gap:8px;box-shadow:4px 4px 0 rgba(255,255,255,.5)}

/* about */
.worker{left:69px;top:887px;width:380px;height:595px;background:linear-gradient(180deg,#f6f6f6,#eaeaea);border-radius:4px}
.about h2{position:absolute;left:522px;top:960px;font-size:30px;font-weight:700;color:var(--ink);line-height:37px}
.about p{position:absolute;left:522px;top:1066px;width:610px;font-size:13px;line-height:22px;color:var(--text)}
.learn{position:absolute;font-size:14px;font-weight:700;color:var(--red)}
.stats{position:absolute;left:522px;top:1298px;width:608px;height:96px;background:var(--light);display:flex}
.stat{flex:1;display:flex;align-items:center;justify-content:space-between;padding:0 24px;border-right:1px solid var(--line)}
.stat:last-child{border-right:0}
.stat b{display:block;font-size:26px;color:var(--ink);font-weight:700}
.stat span{font-size:13px;color:var(--muted)}

/* appointment */
.appoint{position:absolute;left:0;top:1544px;width:1200px;height:192px;background:var(--light)}
.appoint h3{position:absolute;left:69px;top:44px;font-size:21px;font-weight:700;color:var(--ink)}
.appoint p{position:absolute;left:69px;top:94px;width:320px;font-size:13px;line-height:18px;color:var(--muted)}
.field{position:absolute;width:224px;height:36px;border:1px solid #cfcfcf;background:var(--white);font-size:12px;color:#999;padding:10px 18px}
.send{position:absolute;left:906px;top:111px;width:224px;height:36px;background:var(--red);color:var(--white);font-size:13px;font-weight:700;display:flex;align-items:center;justify-content:center}

/* section titles */
.sec-title{position:absolute;left:0;width:1200px;text-align:center;font-size:30px;font-weight:700;color:var(--ink)}
.sec-sub{position:absolute;left:0;width:1200px;text-align:center;font-size:15px;color:var(--text)}

/* services */
.services{position:absolute;left:0;top:1736px;width:1200px;height:660px;background:linear-gradient(180deg,#fff 0%,#f7f7f7 40%,#f2f2f2 100%)}
.svc{position:absolute;width:250px}
.svc h4{font-size:16px;font-weight:700;color:var(--ink);margin-bottom:10px}
.svc p{font-size:13px;line-height:17px;color:var(--text)}
.svc.left{text-align:right}
.num{position:absolute;font-size:66px;font-weight:400;color:var(--red-soft);line-height:1}
.center-car{left:403px;top:2003px;width:392px;height:261px;background:radial-gradient(ellipse at 50% 55%,#e3262c 0%,#a9121a 55%,rgba(169,18,26,0) 72%)}

/* testimonials */
.testi{position:absolute;left:0;top:2396px;width:1200px;height:338px;background:linear-gradient(180deg,#262626,#171717)}
.tcard{position:absolute;top:73px;width:514px;height:167px;background:var(--white)}
.avatar{position:absolute;left:39px;top:44px;width:78px;height:78px;border-radius:50%;background:linear-gradient(135deg,#d9c4b6,#8a6f5e);border:3px solid #eee}
.quote{position:absolute;left:100px;top:42px;width:22px;height:22px;border-radius:50%;background:var(--red);color:var(--white);font-size:18px;font-weight:700;text-align:center;line-height:26px}
.tcard .divider{position:absolute;left:131px;top:24px;width:1px;height:120px;background:var(--line)}
.tcard p{position:absolute;left:154px;top:24px;width:340px;font-size:12px;font-style:italic;line-height:18px;color:var(--muted)}
.tcard b{position:absolute;left:154px;top:136px;font-size:11px;color:var(--ink)}

/* speciality */
.tab{position:absolute;top:2903px;height:31px;font-size:11px;font-weight:700;display:flex;align-items:center;justify-content:center;background:#ececec;color:#444}
.tab.on{background:var(--red);color:var(--white)}
.g1{background:linear-gradient(160deg,#7a7f86,#2c3a5a)}
.g2{background:linear-gradient(160deg,#4a4a4a,#a5a5a5)}
.g3{background:linear-gradient(160deg,#2c4f8a,#b23a2a)}
.g4{background:linear-gradient(160deg,#9bb3c8,#3a5a8a)}
.g5{background:linear-gradient(160deg,#3b3d40,#c56a2a)}
.g6{background:linear-gradient(160deg,#6a6a6a,#2a2a2a)}

/* before after */
.before{left:0;top:3763px;width:1200px;height:526px;background:linear-gradient(160deg,#8a8f94,#2a2d31);clip-path:polygon(0 0,625px 0,565px 100%,0 100%)}
.after{left:0;top:3763px;width:1200px;height:526px;background:linear-gradient(160deg,#5e6a74,#1e2226);clip-path:polygon(635px 0,100% 0,100% 100%,575px 100%)}
.ribbon{position:absolute;background:var(--red);color:var(--white);font-size:40px;font-weight:700;display:flex;align-items:center;justify-content:center}
.ba-arrow{position:absolute;top:4238px;width:66px;height:40px;background:var(--red);display:flex;align-items:center;justify-content:center}

/* blog */
.bcard{position:absolute;top:4435px;width:341px;height:449px;background:var(--white);border:1px solid #ececec}
.bcard .img{position:absolute;left:0;top:0;width:100%;height:230px}
.date{position:absolute;left:28px;top:146px;width:66px;height:84px;background:var(--white);text-align:center}
.date b{display:block;height:42px;background:var(--red);color:var(--white);font-size:22px;line-height:42px}
.date span{font-size:15px;line-height:42px;color:var(--ink)}
.bcard h5{position:absolute;left:28px;top:270px;font-size:17px;font-weight:500;color:var(--ink)}
.bcard h5.red{color:var(--red)}
.bcard p{position:absolute;left:28px;top:310px;width:290px;font-size:11px;line-height:24px;color:#999}

/* newsletter */
.news{position:absolute;left:0;top:4942px;width:1200px;height:75px;background:var(--red)}
.news .icon{position:absolute;left:73px;top:17px;width:42px;height:42px;border-radius:50%;border:2px solid var(--white);display:flex;align-items:center;justify-content:center}
.news h3{position:absolute;left:140px;top:21px;font-size:26px;font-weight:700;color:var(--white)}
.news .mail{position:absolute;left:380px;top:21px;width:257px;height:36px;border:2px solid var(--white);color:var(--white);font-size:11px;font-weight:700;padding:10px 16px}
.news .sign{position:absolute;left:657px;top:21px;width:186px;height:36px;border:2px solid var(--white);color:var(--white);font-size:12px;font-weight:700;display:flex;align-items:center;justify-content:center}
.news .circ{position:absolute;top:23px;width:30px;height:30px;border-radius:50%;border:2px solid var(--white)}

/* footer */
.footer{position:absolute;left:0;top:5017px;width:1200px;height:359px;background:var(--footer);color:#ddd}
.footer h6{position:absolute;top:40px;font-size:16px;font-weight:700;color:var(--white)}
.footer h6:after{content:"";position:absolute;left:0;bottom:-10px;width:30px;height:2px;background:var(--red)}
.footer .col{position:absolute;top:82px;font-size:13px;line-height:28px;color:#ddd}
.footer .about-text{position:absolute;left:69px;top:82px;width:270px;font-size:13px;line-height:17px}
.contact-line{position:absolute;left:69px;font-size:13px;display:flex;gap:10px;line-height:17px}
.post{position:absolute;left:837px;width:293px;height:94px}
.post .t{position:absolute;left:0;top:0;width:190px;font-size:12px;font-weight:700;color:var(--white);line-height:15px}
.post .s{position:absolute;left:0;top:42px;width:190px;font-size:10px;font-weight:700;color:#ccc;line-height:12px}
.post .th{position:absolute;left:198px;top:0;width:95px;height:94px;background:linear-gradient(150deg,#6b7380,#1f2a3a)}
</style>
</head>
<body>

<!-- top bar -->
<div class="topbar">
  <div class="follow">Follow With Us: <span class="dot"></span><span class="dot"></span><span class="dot"></span><span class="dot"></span></div>
  <div class="right">
    <span>
      <svg width="9" height="11" viewBox="0 0 10 12"><path d="M5 0a4 4 0 0 0-4 4c0 3 4 8 4 8s4-5 4-8a4 4 0 0 0-4-4z" fill="#fff"/><circle cx="5" cy="4" r="1.5" fill="#111"/></svg>
      Store Locator</span>
    <span>
      <svg width="11" height="11" viewBox="0 0 12 12"><path d="M6 0l1.8 3.8 4.2.5-3.1 2.9.8 4.1L6 9.3 2.3 11.3l.8-4.1L0 4.3l4.2-.5z" fill="#fff"/></svg>
      WE Are Different</span>
  </div>
  <div class="search"><svg width="16" height="16" viewBox="0 0 16 16"><circle cx="6.5" cy="6.5" r="5" fill="none" stroke="#fff" stroke-width="2"/><path d="M10 10l5 5" stroke="#fff" stroke-width="2"/></svg></div>
</div>

<!-- header -->
<header class="header">
  <div class="logo-block"></div>
  <div class="brand">BRIGHTGATE</div>
  <div class="info" style="left:600px">
    <svg width="32" height="34" viewBox="0 0 32 34"><path d="M4 32L14 4h4l10 28" fill="none" stroke="#ee1c25" stroke-width="3"/><path d="M9 20h14" stroke="#ee1c25" stroke-width="3"/></svg>
    <div><b>Opening Hours</b><i>8:00AM - 5:00PM</i></div>
  </div>
  <div class="info" style="left:872px">
    <svg width="34" height="34" viewBox="0 0 34 34"><path d="M5 20v-4a12 12 0 0 1 24 0v4" fill="none" stroke="#ee1c25" stroke-width="2.5"/><rect x="3" y="18" width="6" height="10" rx="2" fill="#ee1c25"/><rect x="25" y="18" width="6" height="10" rx="2" fill="#ee1c25"/></svg>
    <div><b>Support <span style="font-weight:400">209.555.0148</span></b><span><b style="display:inline">Email:</b> hello@brightgate-auto.example</span></div>
  </div>
</header>

<!-- nav -->
<nav class="nav">
  <a class="active" style="left:71px">HOME</a>
  <a style="left:173px">ABOUT US</a>
  <a style="left:298px">LOCATION</a>
  <a style="left:428px">SERVICES</a>
  <a style="left:553px">CONTACT US</a>
  <div class="book">BOOK NOW</div>
</nav>

<!-- hero -->
<section class="hero" role="img" aria-label="Red sports car on a dark blue background with glowing light particles">
  <div class="car"></div>
  <h1>Personal Care<br>And Maintenance Service</h1>
  <p>Lorem Ipsum is simply dummy text of the printing and typesetting industry. Lorem Ipsum has been the industry's standard dummy text ever since the 1500s</p>
  <div class="btn-outline">Learn More <svg width="8" height="10" viewBox="0 0 8 10"><path d="M2 1l4 4-4 4" fill="none" stroke="#ee1c25" stroke-width="1.6"/></svg></div>
</section>

<!-- about -->
<section class="about">
  <div class="photo worker" role="img" aria-label="Mechanic in red overalls holding a wrench, one foot resting on a stack of tyres"></div>
  <h2>WE HAVE 25 YEARS<br>OF EXPERIENCE IN THIS FIELD</h2>
  <p>Marco Ellery, Owner, has been in the auto body repair industry for 13 years. Our shop uses the latest technologies to make sure your vehicle is repaired the correct way. Our staff constantly attends classes for AutoSkill which educates us in the new technologies available for the repair process and newest cars. We learn about new materials and repair processes to effectively bring your car back to the way it was before the damage occurred.</p>
  <div class="learn" style="left:522px;top:1223px">Learn More &nbsp;›</div>
  <div class="stats">
    <div class="stat"><div><b>3500+</b><span>Services</span></div>
      <svg width="34" height="38" viewBox="0 0 34 38"><circle cx="17" cy="12" r="7" fill="none" stroke="#aaa" stroke-width="2"/><path d="M17 19v17M12 28h10" stroke="#aaa" stroke-width="2"/></svg></div>
    <div class="stat"><div><b>200+</b><span>Engineers</span></div>
      <svg width="36" height="38" viewBox="0 0 36 38"><path d="M8 14a10 10 0 0 1 20 0z" fill="none" stroke="#aaa" stroke-width="2"/><circle cx="18" cy="19" r="6" fill="none" stroke="#aaa" stroke-width="2"/><path d="M5 37a13 11 0 0 1 26 0" fill="none" stroke="#aaa" stroke-width="2"/></svg></div>
    <div class="stat"><div><b>1450+</b><span>Happy Clients</span></div>
      <svg width="36" height="36" viewBox="0 0 36 36"><circle cx="18" cy="18" r="15" fill="none" stroke="#aaa" stroke-width="2"/><path d="M11 18l5 5 10-11" fill="none" stroke="#aaa" stroke-width="2"/></svg></div>
  </div>
</section>

<!-- appointment -->
<section class="appoint">
  <h3>MAKE AN APPOINTMENT</h3>
  <p>They call him Flipper Flipper faster than lite no one you see is smarter.</p>
  <div class="field" style="left:419px;top:46px">Full Name</div>
  <div class="field" style="left:660px;top:46px">Email Address</div>
  <div class="field" style="left:906px;top:46px">Phone</div>
  <div class="field" style="left:419px;top:111px">Select Date</div>
  <div class="field" style="left:660px;top:111px">Select Category</div>
  <div class="send">SEND NOW</div>
</section>

<!-- services -->
<section class="services"></section>
<div class="sec-title" style="top:1792px">OUR SERVICES</div>
<div class="sec-sub" style="top:1846px">They call him Flipper Flipper faster than lite no one you see is smarter.</div>
<div class="svc left" style="left:63px;top:1942px"><h4>BRAKES &amp; BRAKE REPAIR</h4><p>After checking on everyone's safety, administering first aid and calling emergency services if .</p></div>
<div class="num" style="left:336px;top:1936px">1</div>
<div class="svc" style="left:883px;top:1942px"><h4>TIRE MAINTENANCE</h4><p>Have a chip or crack in your auto glass? Poor driving conditions or even bad weathe.</p></div>
<div class="num" style="left:816px;top:1936px">2</div>
<div class="svc left" style="left:63px;top:2200px"><h4>SHOP FOR TIRES</h4><p>Welcome to Northway 24 Hour Towing! We are your choice for fast, affordable and .</p></div>
<div class="num" style="left:336px;top:2194px">3</div>
<div class="svc" style="left:883px;top:2200px"><h4>STEERING &amp; SUSPENSION</h4><p>Body &amp; Paint Center Of Linden is a full service Auto Body Shop, Collision repair specialist .</p></div>
<div class="num" style="left:816px;top:2194px">4</div>
<div class="photo center-car" role="img" aria-label="Front view of a red sports car"></div>
<svg class="abs" style="left:56px;top:2082px" width="36" height="62" viewBox="0 0 36 62"><path d="M32 2L4 31l28 29" fill="none" stroke="#ee1c25" stroke-width="3"/></svg>
<svg class="abs" style="left:1100px;top:2082px" width="36" height="62" viewBox="0 0 36 62"><path d="M4 2l28 29L4 60" fill="none" stroke="#ee1c25" stroke-width="3"/></svg>

<!-- testimonials -->
<section class="testi">
  <div class="tcard" style="left:69px">
    <div class="avatar" role="img" aria-label="Customer portrait"></div><div class="quote">“</div>
    <div class="divider"></div>
    <p>Picked my car up yesterday and they are absolutely wonderful people especially...they went over and beyond for me! And their customer service skills are impeccable! I would recommend them to everyone! Thank you again for your amazing work!</p>
    <b>MIRABEL</b>
  </div>
  <div class="tcard" style="left:616px">
    <div class="avatar" role="img" aria-label="Customer portrait"></div><div class="quote">“</div>
    <div class="divider"></div>
    <p>Brought my wife's car to Fairline Auto Body Shop that was vandalized at here work parking lot. Their service was amazing and I was very satisfied with their performance. This shop is highly recommended. Thanks guys!!!</p>
    <b>TORIN</b>
  </div>
  <svg class="abs" style="left:388px;top:270px" width="24" height="42" viewBox="0 0 24 42"><path d="M21 2L3 21l18 19" fill="none" stroke="#ee1c25" stroke-width="2.5"/></svg>
  <svg class="abs" style="left:783px;top:270px" width="24" height="42" viewBox="0 0 24 42"><path d="M3 2l18 19L3 40" fill="none" stroke="#ee1c25" stroke-width="2.5"/></svg>
</section>

<!-- speciality -->
<div class="sec-title" style="top:2790px">OUR SPECIALITY</div>
<div class="sec-sub" style="top:2844px">They call him Flipper Flipper faster than lite no one you see is smarter.</div>
<div class="tab on" style="left:234px;width:75px">ALL</div>
<div class="tab" style="left:326px;width:146px">AUTO BODY REPAIR</div>
<div class="tab" style="left:490px;width:147px">AUTO GLAS REPAIR</div>
<div class="tab" style="left:653px;width:146px">BODY AND PANT</div>
<div class="tab" style="left:816px;width:150px">FRAME STRAIGTENING</div>
<div class="photo g1" style="left:69px;top:2980px;width:334px;height:443px" role="img" aria-label="Mechanic inspecting a brake disc under a lifted car"></div>
<div class="photo g2" style="left:432px;top:2980px;width:334px;height:209px" role="img" aria-label="Hands holding a gearbox shaft"></div>
<div class="photo g3" style="left:432px;top:3218px;width:334px;height:205px" role="img" aria-label="Mechanic in a workshop beside a car"></div>
<div class="photo g4" style="left:795px;top:2980px;width:335px;height:443px" role="img" aria-label="Mechanic using an impact wrench on a wheel"></div>
<div class="photo g5" style="left:69px;top:3454px;width:697px;height:209px" role="img" aria-label="Gloved hands attaching jumper cables in an engine bay"></div>
<div class="photo g6" style="left:795px;top:3454px;width:335px;height:209px" role="img" aria-label="Technician running car diagnostics on a laptop"></div>

<!-- before / after -->
<div class="photo before" role="img" aria-label="Damaged black SUV before repair"></div>
<div class="photo after" role="img" aria-label="Black SUV restored after repair"></div>
<div class="ribbon" style="left:-40px;top:4145px;width:240px;height:60px;transform:rotate(45deg)">Before</div>
<div class="ribbon" style="left:1000px;top:3810px;width:240px;height:60px;transform:rotate(45deg)">After</div>
<div class="ba-arrow" style="left:488px"><svg width="20" height="14" viewBox="0 0 20 14"><path d="M19 7H2M8 1L2 7l6 6" fill="none" stroke="#fff" stroke-width="2"/></svg></div>
<div class="ba-arrow" style="left:562px"><svg width="20" height="14" viewBox="0 0 20 14"><path d="M1 7h17M12 1l6 6-6 6" fill="none" stroke="#fff" stroke-width="2"/></svg></div>

<!-- blog -->
<div class="sec-title" style="top:4337px">LATEST BLOG</div>
<div class="sec-sub" style="top:4391px">They call him Flipper Flipper faster than lite no one you see is smarter.</div>
<article class="bcard" style="left:69px">
  <div class="img g1" role="img" aria-label="Two mechanics talking in a garage"></div>
  <div class="date"><b>01</b><span>Feb</span></div>
  <h5>The Word Impossible</h5>
  <p>Lorem ipsum dolor sit amet, consectetur adipisicing elit. Molestias adipisci voluptate qui laudantium vitae? Impedit pariatur molestiae officia saepe atque. Illum quos maxime maiores, inventore eveniet? Iure, fuga quis. Magni.</p>
</article>
<article class="bcard" style="left:430px">
  <div class="img g3" role="img" aria-label="Mechanic working under a lifted car"></div>
  <div class="date"><b>22</b><span>Mar</span></div>
  <h5 class="red">Flipper Faster</h5>
  <p>Lorem ipsum dolor sit amet, consectetur adipisicing elit. Molestias adipisci voluptate qui laudantium vitae? Impedit pariatur molestiae officia saepe atque. Illum quos maxime maiores, inventore eveniet? Iure, fuga quis. Magni.</p>
</article>
<article class="bcard" style="left:789px">
  <div class="img" style="background:linear-gradient(150deg,#c0262c,#2a3550)" role="img" aria-label="Mechanic checking a red car"></div>
  <div class="date"><b>28</b><span>Apr</span></div>
  <h5>How to boost up your vehicle engine</h5>
  <p>Lorem ipsum dolor sit amet, consectetur adipisicing elit. Molestias adipisci voluptate qui laudantium vitae? Impedit pariatur molestiae officia saepe atque. Illum quos maxime maiores, inventore eveniet? Iure, fuga quis. Magni.</p>
</article>

<!-- newsletter -->
<section class="news">
  <div class="icon"><svg width="20" height="14" viewBox="0 0 20 14"><rect x="1" y="1" width="18" height="12" fill="none" stroke="#fff" stroke-width="1.6"/><path d="M1 1l9 7 9-7" fill="none" stroke="#fff" stroke-width="1.6"/></svg></div>
  <h3>Newsletter</h3>
  <div class="mail">Your mail</div>
  <div class="sign">SIGN UP</div>
  <div class="circ" style="left:902px"></div>
  <div class="circ" style="left:950px"></div>
  <div class="circ" style="left:998px"></div>
  <div class="circ" style="left:1046px"></div>
  <div class="circ" style="left:1094px"></div>
</section>

<!-- footer -->
<footer class="footer">
  <h6 style="left:69px">WE GIVE BEST SERVICES</h6>
  <div class="about-text">One of our Bhutan destination expert will be dropping you an email for an obligation free consultation.</div>
  <div class="contact-line" style="top:142px"><svg width="14" height="14" viewBox="0 0 14 14"><path d="M3 1l2 3-1.5 1.5a8 8 0 0 0 5 5L10 9l3 2-1 2C6 13 1 8 1 2z" fill="#fff"/></svg>209.555.0148</div>
  <div class="contact-line" style="top:178px"><svg width="12" height="15" viewBox="0 0 10 12"><path d="M5 0a4 4 0 0 0-4 4c0 3 4 8 4 8s4-5 4-8a4 4 0 0 0-4-4z" fill="#fff"/><circle cx="5" cy="4" r="1.5" fill="#151515"/></svg><span>18 Alder Crest Road<br>Stockton, CA 95204</span></div>

  <h6 style="left:440px">QUICK LINKS</h6>
  <div class="col" style="left:440px">Home<br>About Us<br>Services<br>Gallery<br>Testimonials<br>Request Form<br>Contact Us</div>

  <h6 style="left:649px">LEGAL</h6>
  <div class="col" style="left:649px;line-height:36px">Privacy Policy<br>Terms &amp; Conditions<br>Legal Notice</div>

  <h6 style="left:837px">LATEST POSTS</h6>
  <div class="post" style="top:81px"><div class="t">They call him Flipper Flipper see is smarter.</div><div class="s">Lorem Ipsum is simply dummy text of the printing and typesetting industry.</div><div class="th" role="img" aria-label="Mechanic working on an engine"></div></div>
  <div class="post" style="top:202px"><div class="t">They call him Flipper Flipper see is smarter.</div><div class="s">Lorem Ipsum is simply dummy text of the printing and typesetting industry.</div><div class="th" role="img" aria-label="Mechanic beside a car"></div></div>
</footer>

</body>
</html>
```